Wordpress website update with basic ecomm features

We need an update to our existing website
www.brightmoorhub.com.au that can be easily updated, enhances our logo and can take payments online and a basic text logo suite for 3 products. Website would reflect confidence and give clients confidence in the outcomes we will provide for them. must be easy to use, crisp, fresh, clean and dynamic.

Target Market(s)

entrepreneurs, professionals, small business owners, corporate organisations, universities

Industry/Entity Type

Online

Coding

Coded - Design and coding required

Number of Pages Required

5+ page

Font styles to use
Sans Serif

Requirements
Must have
• be easy to navigate, look professional, please see brief doc
Nice to have
• please see briefing doc
Should not have
• please see briefing doc

```html
<!DOCTYPE html>
<html lang="en">
<head>
<meta charset="utf-8">
<title>Brightmoor Hub – Australian Business Entrepreneurship</title>
<link href="https://fonts.googleapis.com/css2?family=Jost:wght@400;500;600;700&family=Open+Sans:wght@400;600&family=Lora:ital@1&display=swap" rel="stylesheet">
<style>
:root{
  --ink:#111;
  --text:#333;
  --muted:#666;
  --line:#e3e3e3;
  --white:#fff;
  --black:#000;
  --footer:#2a2a2a;
  --footer-bottom:#111;
  --footer-text:#ddd;
}
*{box-sizing:border-box;margin:0;padding:0}
html,body{width:1200px;height:2530px;overflow:hidden;background:var(--white)}
body{position:relative;font-family:"Open Sans",sans-serif;color:var(--text)}
.abs{position:absolute}

/* header */
.site-header{position:absolute;left:0;top:0;width:1200px;height:115px;background:var(--white)}
.brand{position:absolute;left:180px;top:14px;width:94px;display:flex;flex-direction:column;align-items:center;gap:6px;font-family:"Jost",sans-serif;font-weight:500;font-size:9.5px;color:var(--ink);letter-spacing:1px;white-space:nowrap}
.brand-mark{width:72px;height:72px;background:var(--black);border-radius:5px}
.nav{position:absolute;left:351px;top:33px;height:41px;display:flex;align-items:center;font-family:"Jost",sans-serif;font-size:11px;font-weight:500;letter-spacing:.5px}
.nav a{color:var(--ink);text-decoration:none;margin-right:46px}
.nav a.active{background:var(--black);color:var(--white);width:81px;text-align:center;line-height:41px;border-radius:3px;margin-right:30px}
.phone{position:absolute;left:820px;top:38px;display:flex;align-items:center;gap:10px;font-family:"Jost",sans-serif;font-size:23px;color:var(--ink)}

/* hero */
.hero{position:absolute;left:0;top:115px;width:1200px;height:505px;background:radial-gradient(ellipse at 70% 30%,#f3ece7 0%,#d9ccc7 40%,#a8908c 75%,#6e5a5a 100%)}
.hero-title{position:absolute;left:221px;top:170px;width:758px;height:44px;background:rgba(20,20,20,.85);color:var(--white);font-family:"Jost",sans-serif;font-size:35px;line-height:44px;text-align:center;letter-spacing:1px;white-space:nowrap}
.hero-date{position:absolute;left:331px;top:226px;width:547px;height:33px;background:var(--white);color:var(--ink);font-family:"Jost",sans-serif;font-size:19px;line-height:33px;text-align:center;white-space:nowrap}
.hero-cta{position:absolute;left:487px;top:286px;width:224px;height:43px;background:var(--black);color:var(--white);font-family:"Jost",sans-serif;font-size:23px;line-height:43px;text-align:center}
.slide-arrow{position:absolute;width:33px;height:73px;background:var(--black);display:flex;align-items:center;justify-content:center}
.dots{position:absolute;left:550px;top:469px;display:flex;gap:3px}
.dots span{width:17px;height:17px;background:var(--black)}
.dots span.on{background:var(--white);border:2px solid var(--black)}

/* intro */
.intro-title{position:absolute;left:0;top:684px;width:1200px;text-align:center;font-family:"Jost",sans-serif;font-size:20px;font-weight:400;letter-spacing:1px;color:var(--ink)}
.intro-title b{font-weight:700}
.intro-text{position:absolute;left:190px;top:726px;width:820px;text-align:center;font-size:14.5px;line-height:27px;color:var(--text)}
.venture{position:absolute;top:819px;width:210px;text-align:center}
.venture svg{display:block;margin:0 auto}
.venture h3{font-family:"Jost",sans-serif;font-size:16px;font-weight:600;color:var(--ink);margin-top:26px;letter-spacing:.5px}
.venture p{font-size:11.5px;line-height:19px;margin:14px auto 0;width:185px;color:var(--text)}

/* section labels */
.rule{position:absolute;left:10px;width:1180px;height:1px;background:var(--line)}
.label{position:absolute;background:var(--black);color:var(--white);font-family:"Jost",sans-serif;font-weight:500;font-size:15px;text-align:center;letter-spacing:.5px}

/* speakers */
.tile{position:absolute;border:1px solid #eee}
.t-warm{background:linear-gradient(160deg,#f2f2f2,#cfb6a0 55%,#8a7060)}
.t-dark{background:linear-gradient(160deg,#eee,#9a8a80 55%,#3b3b40)}
.t-gold{background:linear-gradient(160deg,#f6f0e2,#d9bf83 55%,#b08a52)}
.featured{background:#7d7d7d;color:var(--white);display:flex;flex-direction:column;justify-content:center;align-items:center;text-align:center}
.featured strong{font-family:"Open Sans",sans-serif;font-size:15px;font-weight:600}
.featured span{font-size:14px;line-height:21px;width:290px;margin-top:4px}

/* testimonial */
.partner{position:absolute;left:537px;top:2018px;width:125px;height:61px;border:1px solid #ddd;display:flex;align-items:center;justify-content:center}
.partner i{display:block;width:60px;height:40px;background:#ddd}
.quote{position:absolute;left:260px;top:2104px;width:680px;text-align:center;font-family:"Lora",serif;font-style:italic;font-size:14.5px;line-height:25px;color:var(--muted)}
.quote-mark{position:absolute;left:215px;top:2098px;font-family:"Lora",serif;font-size:34px;color:#aaa}
.cite{position:absolute;left:0;top:2186px;width:1200px;text-align:center;font-size:13px;color:var(--muted)}

/* footer */
.site-footer{position:absolute;left:0;top:2263px;width:1200px;height:216px;background:var(--footer);color:var(--footer-text)}
.col{position:absolute;top:30px}
.col h4{font-family:"Jost",sans-serif;font-size:12.5px;font-weight:600;color:var(--white);letter-spacing:.5px;margin-bottom:18px}
.col p{font-size:10px;line-height:17px}
.btn-outline{display:inline-block;margin-top:14px;border:1px solid #ccc;color:var(--white);font-family:"Jost",sans-serif;font-size:10.5px;padding:5px 10px}
.signup{margin-top:12px;width:230px;border-bottom:1px solid #777;height:20px;position:relative}
.contact-row{display:flex;gap:14px;font-size:9.5px;line-height:15px;margin-bottom:14px}
.contact-row svg{flex:none;margin-top:2px}
.footer-bottom{position:absolute;left:0;top:2479px;width:1200px;height:51px;background:var(--footer-bottom);color:var(--footer-text);font-size:10px;line-height:51px;padding-left:190px}
</style>
</head>
<body>

<header class="site-header">
  <div class="brand"><span class="brand-mark"></span>BRIGHTMOOR HUB</div>
  <nav class="nav">
    <a class="active">HOME</a><a>ABOUT</a><a>FAQ</a><a>TESTIMONIAL</a><a>VENUE</a>
  </nav>
  <div class="phone">
    <svg width="22" height="22" viewBox="0 0 24 24"><path d="M6.6 10.8c1.4 2.8 3.8 5.1 6.6 6.6l2.2-2.2c.3-.3.7-.4 1-.2 1.1.4 2.3.6 3.6.6.6 0 1 .4 1 1V20c0 .6-.4 1-1 1C10.6 21 3 13.4 3 4c0-.6.4-1 1-1h3.5c.6 0 1 .4 1 1 0 1.3.2 2.5.6 3.6.1.3 0 .7-.2 1L6.6 10.8z" fill="none" stroke="#111" stroke-width="2"/></svg>
    1-555-204-7183
  </div>
</header>

<section class="hero" role="img" aria-label="Photo of a stage microphone in front of a blurred conference audience">
  <div class="hero-title">AUSRALIAN BUSINESS ENTREPRENEURSHIP</div>
  <div class="hero-date">NOVEMBER 16-17, 2016 - AUSTRALIAN CONVENTION HALL</div>
  <div class="hero-cta">GET YOUR TICKET</div>
  <div class="slide-arrow" style="left:10px;top:216px"><svg width="12" height="20" viewBox="0 0 12 20"><path d="M10 2L2 10l8 8" fill="none" stroke="#fff" stroke-width="1.5"/></svg></div>
  <div class="slide-arrow" style="left:1157px;top:216px"><svg width="12" height="20" viewBox="0 0 12 20"><path d="M2 2l8 8-8 8" fill="none" stroke="#fff" stroke-width="1.5"/></svg></div>
  <div class="dots"><span></span><span class="on"></span><span></span><span></span><span></span></div>
</section>

<h2 class="intro-title">BRIGHTMOOR HUB TAKES THE BEST FROM THE <b>4 EARLY STAGE</b> VENTURE INSTITUTIONS</h2>
<p class="intro-text">The Brightmoor Hub is focused on individuals with an entrepreneurial mindset and business builders with an appreciation for the entrepreneurial journey.</p>

<div class="venture" style="left:178px">
  <svg width="136" height="136" viewBox="0 0 136 136"><circle cx="68" cy="68" r="63" fill="none" stroke="#333" stroke-width="6" stroke-dasharray="330 66" transform="rotate(-60 68 68)"/><path d="M56 58h24l8 22c0 8-10 10-20 10s-20-2-20-10z" fill="#111"/><text x="68" y="82" font-size="16" fill="#fff" text-anchor="middle" font-family="Jost">$</text><path d="M58 44l10 8 10-8" fill="none" stroke="#111" stroke-width="3"/></svg>
  <h3>INCUBATORS</h3>
  <p>Ut enim ad minim veniam, quis nostrud exercitation ullamco laboris nisi ut aliquip ex ea commodo consequat.</p>
</div>
<div class="venture" style="left:390px">
  <svg width="136" height="136" viewBox="0 0 136 136"><circle cx="68" cy="68" r="63" fill="none" stroke="#333" stroke-width="6" stroke-dasharray="330 66" transform="rotate(-60 68 68)"/><ellipse cx="68" cy="44" rx="12" ry="4" fill="none" stroke="#111" stroke-width="3"/><circle cx="68" cy="62" r="12" fill="#111"/><path d="M52 96l6-22h20l6 22z" fill="#111"/><path d="M56 74c-14-4-18-14-12-20M80 74c14-4 18-14 12-20" fill="none" stroke="#111" stroke-width="3"/></svg>
  <h3>ANGEL INVESTOR</h3>
  <p>Ut enim ad minim veniam, quis nostrud exercitation ullamco laboris nisi ut aliquip ex ea commodo consequat.</p>
</div>
<div class="venture" style="left:600px">
  <svg width="136" height="136" viewBox="0 0 136 136"><circle cx="68" cy="68" r="63" fill="none" stroke="#333" stroke-width="6" stroke-dasharray="330 66" transform="rotate(-60 68 68)"/><path d="M90 40c-16 2-28 14-32 30l8 8c16-4 28-16 30-32z" fill="#111"/><path d="M58 70l-10 2-6 8 12-1M66 78l-2 10-8 6 1-12" fill="#111"/><path d="M52 84c-6 2-8 8-8 10 2 0 8-2 10-8" fill="none" stroke="#111" stroke-width="2"/></svg>
  <h3>ACCELERATORS</h3>
  <p>Ut enim ad minim veniam, quis nostrud exercitation ullamco laboris nisi ut aliquip ex ea commodo consequat.</p>
</div>
<div class="venture" style="left:812px">
  <svg width="136" height="136" viewBox="0 0 136 136"><circle cx="68" cy="68" r="63" fill="none" stroke="#333" stroke-width="6" stroke-dasharray="330 66" transform="rotate(-60 68 68)"/><path d="M56 46h18M60 46v16L46 86c-2 4 0 8 4 8h32c4 0 6-4 4-8L72 62V46" fill="none" stroke="#111" stroke-width="3"/><path d="M52 80h30l4 8H48z" fill="#111"/><circle cx="86" cy="44" r="4" fill="none" stroke="#111" stroke-width="2"/><circle cx="80" cy="54" r="2.5" fill="#111"/></svg>
  <h3>HYBRIDS</h3>
  <p>Ut enim ad minim veniam, quis nostrud exercitation ullamco laboris nisi ut aliquip ex ea commodo consequat.</p>
</div>

<div class="rule" style="top:1188px"></div>
<div class="label" style="left:514px;top:1167px;width:172px;height:43px;line-height:43px">OUR SPEAKERS</div>

<div class="tile t-warm" style="left:14px;top:1267px;width:387px;height:291px" role="img" aria-label="Speaker portrait"></div>
<div class="tile featured" style="left:403px;top:1267px;width:386px;height:291px" role="img" aria-label="Featured speaker portrait with caption">
  <strong>Daniel Marsh</strong>
  <span>Former Trade Minister of the Commonwealth &amp; Climate Advocate</span>
</div>
<div class="tile t-dark" style="left:792px;top:1267px;width:194px;height:194px" role="img" aria-label="Speaker portrait"></div>
<div class="tile t-warm" style="left:989px;top:1267px;width:197px;height:144px" role="img" aria-label="Speaker portrait"></div>
<div class="tile t-warm" style="left:989px;top:1414px;width:197px;height:141px" role="img" aria-label="Speaker portrait"></div>
<div class="tile t-gold" style="left:792px;top:1462px;width:194px;height:197px" role="img" aria-label="Speaker portrait"></div>
<div class="tile t-warm" style="left:989px;top:1557px;width:197px;height:135px" role="img" aria-label="Speaker portrait"></div>
<div class="tile t-dark" style="left:792px;top:1661px;width:194px;height:156px" role="img" aria-label="Speaker portrait"></div>
<div class="tile t-warm" style="left:14px;top:1560px;width:192px;height:197px" role="img" aria-label="Speaker portrait"></div>
<div class="tile t-dark" style="left:209px;top:1560px;width:386px;height:295px" role="img" aria-label="Speaker portrait"></div>
<div class="tile t-dark" style="left:598px;top:1560px;width:191px;height:197px" role="img" aria-label="Speaker portrait"></div>

<div class="rule" style="top:1944px"></div>
<div class="label" style="left:521px;top:1920px;width:158px;height:50px;line-height:50px">TESTIMONIAL</div>

<div class="partner" aria-label="Northline Advisory Group"><i></i></div>
<div class="slide-arrow" style="left:10px;top:2100px;height:44px"><svg width="12" height="20" viewBox="0 0 12 20"><path d="M10 2L2 10l8 8" fill="none" stroke="#fff" stroke-width="1.5"/></svg></div>
<div class="slide-arrow" style="left:1157px;top:2100px;height:44px"><svg width="12" height="20" viewBox="0 0 12 20"><path d="M2 2l8 8-8 8" fill="none" stroke="#fff" stroke-width="1.5"/></svg></div>
<div class="quote-mark">&ldquo;</div>
<p class="quote">Lorem ipsum dolor sit amet, consectetur adipiscing elit, sed do eiusmod tempor incididunt ut labore et dolore magna aliqua. Ut enim ad minim veniam, quis nostrud exercitation ullamco laboris nisi ut aliquip ex ea commodo consequat.</p>
<p class="cite">- Northline Advisory Group -</p>

<footer class="site-footer">
  <div class="col" style="left:190px;width:230px">
    <h4>ABOUT US</h4>
    <p>Lorem ipsum dolor sit amet, consectetuer adipiscing elit, sed diam nonummy nibh euismod tincidunt ut laoreet dolore magna aliquam erat volutpat. Ut wisi enim ad minim veniam.</p>
    <span class="btn-outline">LEARN MORE</span>
  </div>
  <div class="col" style="left:470px;width:240px">
    <h4>SUBSCRIBE OUR NEWSLETTER</h4>
    <p>Keep up to date with the latest events and get some information about the speakers.</p>
    <div class="signup"><svg class="abs" style="right:2px;top:3px" width="14" height="11" viewBox="0 0 14 11"><rect x="0.5" y="0.5" width="13" height="10" fill="none" stroke="#ccc"/><path d="M1 1l6 5 6-5" fill="none" stroke="#ccc"/></svg></div>
  </div>
  <div class="col" style="left:747px;width:260px">
    <h4>CONTACT INFO</h4>
    <div class="contact-row"><svg width="10" height="13" viewBox="0 0 10 13"><path d="M5 0a5 5 0 0 1 5 5c0 3-5 8-5 8S0 8 0 5a5 5 0 0 1 5-5z" fill="#ddd"/><circle cx="5" cy="5" r="2" fill="#2a2a2a"/></svg><span>48 Harbour Crest Lane, Suite 210<br>Kelby Point, NSW 2480 • AU</span></div>
    <div class="contact-row"><svg width="12" height="12" viewBox="0 0 24 24"><path d="M6.6 10.8c1.4 2.8 3.8 5.1 6.6 6.6l2.2-2.2c.3-.3.7-.4 1-.2 1.1.4 2.3.6 3.6.6.6 0 1 .4 1 1V20c0 .6-.4 1-1 1C10.6 21 3 13.4 3 4c0-.6.4-1 1-1h3.5c.6 0 1 .4 1 1 0 1.3.2 2.5.6 3.6.1.3 0 .7-.2 1z" fill="#ddd"/></svg><span>1-555-204-7183<br>1-555-310-4926</span></div>
    <div class="contact-row"><svg width="12" height="10" viewBox="0 0 12 10"><rect width="12" height="10" fill="#ddd"/><path d="M0 0l6 5 6-5" fill="none" stroke="#2a2a2a"/></svg><span>E-mail: hello@brightmoorhub.</span></div>
  </div>
</footer>
<div class="footer-bottom">Copyright © 2016 brightmoorhub.com.au, All Rights Reserved.</div>

</body>
</html>
```